Help design website for "Verdant Harbor Advisory" to advance the common good

Here is the Google doc link that lays out the design:

https://files.quillmarsh.net/doc/7TrWbnQe48XkLpZa2uMvYcD0sHfGjR35NwoEi9KxyBt/view?mode=share

Here is the Google drive folder with the logos and photos: https://store.quillmarsh.net/open?id=4K9pRtLmWqZx8825BvNcUaYeHs3Jd

The testimonials are being gathered and will be shared by Friday, 1/4.

The winner will also have to migrate the coding files to my hosting site.

Thank you for your help! Looking forward to seeing your designs.

Target Market(s)

Prospective clients

Industry/Entity Type

Non Profit

Coding

Coded - Design and coding required

Number of Pages Required

5+ page

Requirements
Must have
• Noted in the Google doc regarding layout.
Nice to have

```html
<!DOCTYPE html>
<html lang="en">
<head>
<meta charset="utf-8">
<title>Verdant Harbor Advisory</title>
<link href="https://fonts.googleapis.com/css2?family=Montserrat:wght@400;500;600;700&family=Open+Sans:wght@400;600;700&display=swap" rel="stylesheet">
<style>
:root{
  --blue:#4d7cbc;
  --blue-dark:#2f4f80;
  --navy:#27374f;
  --ink:#3a3a3a;
  --muted:#6b6b6b;
  --card:#f1f1f1;
  --line:#d9d9d9;
  --white:#ffffff;
}
*{box-sizing:border-box;margin:0;padding:0}
html,body{width:1200px;height:5310px;overflow:hidden}
body{position:relative;background:var(--white);font-family:"Open Sans",Arial,sans-serif;color:var(--ink)}
section,header,footer{position:absolute;left:0;width:1200px}

/* header */
.site-header{top:0;height:160px;background:var(--white)}
.topbar{position:absolute;right:0;top:0;width:470px;height:40px;background:var(--blue);display:flex;align-items:center;justify-content:flex-end;gap:22px;padding-right:26px;color:var(--white);font-size:13px;font-weight:600}
.topbar .item{display:flex;align-items:center;gap:7px}
.social{display:flex;gap:6px}
.social span{width:18px;height:18px;border:1.5px solid currentColor;border-radius:50%}
.brand{position:absolute;left:40px;top:38px;display:flex;align-items:center;gap:14px}
.brand .mark{width:42px;height:42px;background:var(--blue)}
.brand .name{font-family:"Montserrat",sans-serif;font-weight:600;font-size:23px;letter-spacing:3px;color:var(--navy);line-height:1.15;width:240px}
.main-nav{position:absolute;right:36px;top:98px;display:flex;gap:34px;font-family:"Montserrat",sans-serif;font-weight:700;font-size:14px;letter-spacing:.5px;color:var(--navy)}
.hero{top:160px;height:460px;background:linear-gradient(180deg,#eef0f3 0%,#cfd4db 55%,#aab1bb 100%)}

/* section titles */
.section-title{position:absolute;left:0;width:1200px;text-align:center;font-family:"Montserrat",sans-serif;font-weight:600;font-size:30px;letter-spacing:1.5px;color:var(--navy)}
.section-title em{font-style:normal;color:var(--blue)}
.section-title.light{color:var(--white)}
.section-sub{position:absolute;left:0;width:1200px;text-align:center;font-family:"Montserrat",sans-serif;font-weight:600;font-size:19px;color:var(--navy)}
.section-sub.light{color:var(--white)}

/* about */
.about{top:620px;height:620px}
.about .section-title{top:95px}
.portrait{position:absolute;border-radius:50%;background:radial-gradient(circle at 50% 40%,#c9a48e 0%,#8a7a70 55%,#5c6470 100%);box-shadow:0 0 0 10px #dfe8f4}
.about .portrait{left:72px;top:222px;width:262px;height:262px}
.about-text{position:absolute;left:480px;top:170px;width:670px;font-size:15.5px;line-height:1.55;color:var(--ink)}
.about-text p+p{margin-top:22px}

/* work history */
.work{top:1240px;height:565px;background:linear-gradient(135deg,#4f7cb8 0%,#3e679f 50%,#5a86bf 100%)}
.work .section-title{top:95px}
.logo-grid{position:absolute;left:160px;top:193px;width:884px;display:grid;grid-template-columns:repeat(3,283px);column-gap:17px;row-gap:28px}
.logo-box{height:128px;background:var(--white);display:flex;align-items:center;justify-content:center;gap:12px;font-family:"Montserrat",sans-serif;font-weight:700;font-size:21px;color:var(--navy);text-align:center;padding:0 18px}
.logo-box .dot{width:26px;height:26px;border-radius:50%;background:var(--blue);flex:none}

/* services */
.services{top:1805px;height:1065px}
.services .section-title{top:95px}
.services .section-sub{top:183px}
.card-grid{position:absolute;left:78px;top:260px;display:grid;grid-template-columns:repeat(3,330px);column-gap:27px;row-gap:30px}
.service-card{background:var(--card);height:290px;padding:22px 20px 18px;position:relative}
.service-card.tall{height:460px}
.card-head{display:flex;gap:12px;align-items:flex-start;font-family:"Montserrat",sans-serif;font-weight:700;font-size:16.5px;line-height:1.2;color:var(--navy);min-height:52px}
.card-head svg{flex:none}
.service-card p{margin-top:10px;font-size:13.5px;line-height:1.45;color:var(--muted)}
.testimonial-link{position:absolute;left:0;right:0;bottom:22px;display:flex;justify-content:center;align-items:center;gap:9px;font-family:"Montserrat",sans-serif;font-weight:600;font-size:15px;color:var(--blue)}

/* media */
.media{top:2870px;height:1060px;background:linear-gradient(135deg,#4a78b4 0%,#3b6399 60%,#5280bb 100%)}
.media .section-title{top:95px}
.media .section-sub{top:183px}
.media-grid{position:absolute;left:78px;top:245px;display:grid;grid-template-columns:repeat(3,322px);column-gap:33px}
.media-card{background:var(--white);height:745px;padding:22px 18px;position:relative}
.media-head{display:flex;align-items:center;justify-content:center;gap:12px;font-family:"Montserrat",sans-serif;font-weight:600;font-size:19px;color:var(--navy);margin-bottom:22px}
.media-item{margin-bottom:22px}
.media-item .date{font-family:"Montserrat",sans-serif;font-weight:700;font-size:15px;color:var(--navy)}
.media-item .caption{font-size:14px;line-height:1.35;color:var(--ink);margin:3px 0 10px}
.media-item .caption.strong{font-family:"Montserrat",sans-serif;font-weight:600;font-size:15px;color:var(--navy)}
.media-photo{height:140px;background:linear-gradient(135deg,#8e9aa8,#5f6c7c)}
.media-photo.video{height:230px;background:linear-gradient(135deg,#7c8a7b,#55645a)}
.media-photo.warm{background:linear-gradient(135deg,#a99a8a,#6d6460)}
.load-more{position:absolute;left:0;right:0;bottom:26px;display:flex;flex-direction:column;align-items:center;gap:4px;font-family:"Montserrat",sans-serif;font-weight:700;font-size:15px;color:var(--navy)}

/* contact */
.contact{top:3930px;height:530px}
.contact .heading{position:absolute;left:78px;top:112px;font-family:"Montserrat",sans-serif;font-weight:600;font-size:30px;letter-spacing:1.5px;color:var(--navy)}
.contact-text{position:absolute;left:78px;top:205px;width:500px;font-size:15.5px;line-height:1.5}
.contact-text h3{font-family:"Montserrat",sans-serif;font-weight:700;font-size:16px;color:var(--navy)}
.contact-text p{margin-bottom:18px}
.contact .portrait{left:805px;top:140px;width:300px;height:300px;background:radial-gradient(circle at 50% 45%,#d8d2c6 0%,#9aa2ad 60%,#6f7a88 100%)}

/* message */
.message{top:4460px;height:480px;background:linear-gradient(135deg,#4f7cb8 0%,#3d669e 60%,#5b86be 100%)}
.message .section-title{top:115px}
.form-row{position:absolute;left:140px;top:190px;display:flex;gap:12px}
.field{height:42px;background:rgba(255,255,255,.22);border:1px solid rgba(255,255,255,.35);color:var(--white);font-size:14px;padding:11px 14px}
.form-row .field{width:305px}
.field.textarea{position:absolute;left:140px;top:245px;width:939px;height:150px}
.send-btn{position:absolute;left:487px;top:408px;width:226px;height:46px;border:2px solid var(--white);border-radius:4px;color:var(--white);font-family:"Montserrat",sans-serif;font-weight:600;font-size:16px;display:flex;align-items:center;justify-content:center}

/* footer */
.site-footer{top:4940px;height:370px}
.footer-brand{position:absolute;left:0;width:1200px;top:85px;display:flex;justify-content:center;align-items:center;gap:16px}
.footer-brand .mark{width:50px;height:50px;background:var(--blue)}
.footer-brand .name{font-family:"Montserrat",sans-serif;font-weight:600;font-size:26px;letter-spacing:3px;color:var(--navy);line-height:1.15;width:270px}
.footer-nav{position:absolute;left:0;width:1200px;top:255px;display:flex;justify-content:center;gap:38px;font-family:"Montserrat",sans-serif;font-weight:600;font-size:14px;color:var(--navy)}
.bottom-bar{position:absolute;left:0;top:315px;width:1200px;height:55px;background:#f3f3f3;display:flex;align-items:center;justify-content:space-between;padding:0 20px;font-size:12px;font-weight:600;color:var(--navy)}
.bottom-bar .social span{border-color:var(--navy)}
</style>
</head>
<body>

<header class="site-header">
  <div class="topbar">
    <span class="item">
      <svg width="14" height="14" viewBox="0 0 24 24"><path fill="#fff" d="M6.6 10.8a15.1 15.1 0 0 0 6.6 6.6l2.2-2.2a1 1 0 0 1 1-.25 11.4 11.4 0 0 0 3.6.57 1 1 0 0 1 1 1V20a1 1 0 0 1-1 1A17 17 0 0 1 3 4a1 1 0 0 1 1-1h3.5a1 1 0 0 1 1 1 11.4 11.4 0 0 0 .57 3.6 1 1 0 0 1-.25 1z"/></svg>
      555.010.4420
    </span>
    <span class="item">
      <svg width="16" height="12" viewBox="0 0 16 12"><rect x="0.5" y="0.5" width="15" height="11" fill="none" stroke="#fff"/><path d="M1 1l7 6 7-6" fill="none" stroke="#fff"/></svg>
      hello@verdantharbor.org
    </span>
    <span class="social"><span></span><span></span><span></span></span>
  </div>
  <div class="brand"><span class="mark"></span><span class="name">VERDANT HARBOR ADVISORY</span></div>
  <nav class="main-nav">
    <span>ABOUT</span><span>SERVICES &amp; TESTIMONIALS ▾</span><span>MEDIA &amp; IMPACT ▾</span><span>CONTACT</span>
  </nav>
</header>

<section class="hero" role="img" aria-label="Photo of business people fitting together large puzzle pieces"></section>

<section class="about">
  <h2 class="section-title">ABOUT <em>VERDANT HARBOR</em></h2>
  <div class="portrait" role="img" aria-label="Portrait photo of founder Mara Ellison"></div>
  <div class="about-text">
    <p>Verdant Harbor Advisory supports nonprofit organizations and educational institutions to carry out their missions to benefit the wider community.</p>
    <p>Founder Mara Ellison is an educator with a 22-year record of demonstrated achievement and leadership roles in nonprofits and educational institutions. Most recently, she served as Associate Dean of Students in the University and Director of the Lakeshore Civic Service Center at Lakeshore University. Mara has designed, implemented, and evaluated community-based learning and leadership training programs that have attained positive outcomes documented by survey results, recognition by outside agencies, and grants awarded for new initiatives and expansions. She has also significantly and consistently increased the number of program applicants, volunteers, and community partnerships through innovative programming, improved reputation, targeted recruitment, marketing and communications.</p>
  </div>
</section>

<section class="work" role="img" aria-label="Blue-tinted photo of a team meeting behind the work history">
  <h2 class="section-title light">WORK HISTORY</h2>
  <div class="logo-grid">
    <div class="logo-box">Lakeshore Civic Service Center</div>
    <div class="logo-box"><span class="dot"></span>Pathway Civic</div>
    <div class="logo-box">Summit Ridge Schools</div>
    <div class="logo-box">Neighbor Schools</div>
    <div class="logo-box"><span class="dot"></span>Service Corps</div>
    <div class="logo-box">Bridge Exchange</div>
  </div>
</section>

<section class="services">
  <h2 class="section-title">SERVICES &amp; <em>TESTIMONIALS</em></h2>
  <p class="section-sub">Mara offers consulting services in six areas to support nonprofits and educational institutions.</p>
  <div class="card-grid">
    <article class="service-card">
      <div class="card-head"><svg width="34" height="28" viewBox="0 0 34 28"><circle cx="10" cy="8" r="5" fill="#4d7cbc"/><circle cx="24" cy="8" r="5" fill="#4d7cbc"/><path d="M1 26c0-7 4-10 9-10s9 3 9 10zM15 26c0-7 4-10 9-10s9 3 9 10z" fill="#4d7cbc"/></svg><span>Staff Professional Development</span></div>
      <p>Mara has supervised, coached, and mentored hundreds of staff members, including professionals and students. She uses the "scaffold-model coach-fade" approach to empower and guide her staff in their personal and professional growth. She has led professional development workshops and staff retreats.</p>
      <div class="testimonial-link"><svg width="24" height="24" viewBox="0 0 24 24"><circle cx="12" cy="12" r="10.5" fill="none" stroke="#4d7cbc" stroke-width="2"/><circle cx="8" cy="12" r="1.5" fill="#4d7cbc"/><circle cx="12" cy="12" r="1.5" fill="#4d7cbc"/><circle cx="16" cy="12" r="1.5" fill="#4d7cbc"/></svg>View Testimonials</div>
    </article>
    <article class="service-card">
      <div class="card-head"><svg width="34" height="28" viewBox="0 0 34 28"><circle cx="17" cy="6" r="5" fill="#4d7cbc"/><circle cx="5" cy="12" r="4" fill="#4d7cbc"/><circle cx="29" cy="12" r="4" fill="#4d7cbc"/><path d="M8 27c0-8 4-11 9-11s9 3 9 11z" fill="#4d7cbc"/></svg><span>Community Partnership Development</span></div>
      <p>Mara has collaborated with more than 250 nonprofits, schools, government agencies, and businesses with corporate social responsibility units to create mutually beneficial partnerships. These relationships have been strengthened and sustained to expand programming and initiatives that meet community engagement outcomes.</p>
      <div class="testimonial-link"><svg width="24" height="24" viewBox="0 0 24 24"><circle cx="12" cy="12" r="10.5" fill="none" stroke="#4d7cbc" stroke-width="2"/><circle cx="8" cy="12" r="1.5" fill="#4d7cbc"/><circle cx="12" cy="12" r="1.5" fill="#4d7cbc"/><circle cx="16" cy="12" r="1.5" fill="#4d7cbc"/></svg>View Testimonials</div>
    </article>
    <article class="service-card">
      <div class="card-head"><svg width="34" height="28" viewBox="0 0 34 28"><circle cx="9" cy="7" r="5" fill="#4d7cbc"/><circle cx="25" cy="7" r="5" fill="#4d7cbc"/><rect x="2" y="16" width="30" height="10" rx="3" fill="#4d7cbc"/></svg><span>Group Facilitation &amp; Leadership Training</span></div>
      <p>Mara has facilitated student groups, experiential learning activities, and dialogues on social justice issues, such as power and privilege, education, and poverty. She has developed curriculum and lesson plans for students to gain essential civic leadership competencies.</p>
      <div class="testimonial-link"><svg width="24" height="24" viewBox="0 0 24 24"><circle cx="12" cy="12" r="10.5" fill="none" stroke="#4d7cbc" stroke-width="2"/><circle cx="8" cy="12" r="1.5" fill="#4d7cbc"/><circle cx="12" cy="12" r="1.5" fill="#4d7cbc"/><circle cx="16" cy="12" r="1.5" fill="#4d7cbc"/></svg>View Testimonials</div>
    </article>
    <article class="service-card tall">
      <div class="card-head"><svg width="30" height="30" viewBox="0 0 30 30"><circle cx="12" cy="7" r="5" fill="#4d7cbc"/><path d="M3 28c0-9 4-13 9-13s9 4 9 13z" fill="#4d7cbc"/><rect x="21" y="4" width="8" height="10" fill="#4d7cbc"/></svg><span>Program Design, Implementation, &amp; Evaluation</span></div>
      <p>Mara has launched several programs that take into account best practices, as well as particular institutional cultures, participant demographics, and geographical location. The evaluation data of these programs have demonstrated their impact, and she has secured funding and developed key partnerships for program expansion.</p>
      <div class="testimonial-link"><svg width="24" height="24" viewBox="0 0 24 24"><circle cx="12" cy="12" r="10.5" fill="none" stroke="#4d7cbc" stroke-width="2"/><circle cx="8" cy="12" r="1.5" fill="#4d7cbc"/><circle cx="12" cy="12" r="1.5" fill="#4d7cbc"/><circle cx="16" cy="12" r="1.5" fill="#4d7cbc"/></svg>View Testimonials</div>
    </article>
    <article class="service-card tall">
      <div class="card-head"><svg width="30" height="30" viewBox="0 0 30 30"><rect x="2" y="5" width="26" height="23" rx="2" fill="#4d7cbc"/><rect x="7" y="1" width="3" height="7" fill="#4d7cbc"/><rect x="20" y="1" width="3" height="7" fill="#4d7cbc"/><path d="M15 12l2 4 4 .5-3 3 .8 4-3.8-2-3.8 2 .8-4-3-3 4-.5z" fill="#fff"/></svg><span>Event Planning</span></div>
      <p>Mara has planned events of all sizes that bring together students, staff, faculty, alumni, community partners, funders, and residents for dialogue and service.</p>
      <div class="testimonial-link"><svg width="24" height="24" viewBox="0 0 24 24"><circle cx="12" cy="12" r="10.5" fill="none" stroke="#4d7cbc" stroke-width="2"/><circle cx="8" cy="12" r="1.5" fill="#4d7cbc"/><circle cx="12" cy="12" r="1.5" fill="#4d7cbc"/><circle cx="16" cy="12" r="1.5" fill="#4d7cbc"/></svg>View Testimonials</div>
    </article>
    <article class="service-card tall">
      <div class="card-head"><svg width="30" height="30" viewBox="0 0 30 30"><rect x="3" y="18" width="6" height="10" fill="#4d7cbc"/><rect x="12" y="12" width="6" height="16" fill="#4d7cbc"/><rect x="21" y="5" width="6" height="23" fill="#4d7cbc"/></svg><span>Strategic Planning &amp; Visioning</span></div>
      <p>At Lakeshore University, Mara established and managed a 16-member Advisory Board, including undergraduates, graduate students, faculty, campus colleagues, community partners, and alumni. She has also served on nonprofit and higher education boards to inform their strategic priorities, goals, and allocation of funding and resources.</p>
      <div class="testimonial-link"><svg width="24" height="24" viewBox="0 0 24 24"><circle cx="12" cy="12" r="10.5" fill="none" stroke="#4d7cbc" stroke-width="2"/><circle cx="8" cy="12" r="1.5" fill="#4d7cbc"/><circle cx="12" cy="12" r="1.5" fill="#4d7cbc"/><circle cx="16" cy="12" r="1.5" fill="#4d7cbc"/></svg>View Testimonials</div>
    </article>
  </div>
</section>

<section class="media" role="img" aria-label="Blue-tinted photo of a community gathering behind the media section">
  <h2 class="section-title light">MEDIA &amp; IMPACT</h2>
  <p class="section-sub light">Here is the media coverage for the programs and events that Mara oversaw.</p>
  <div class="media-grid">
    <article class="media-card">
      <div class="media-head"><svg width="26" height="30" viewBox="0 0 26 30"><rect x="1" y="1" width="24" height="28" rx="2" fill="none" stroke="#4d7cbc" stroke-width="2"/><path d="M6 9h14M6 14h14M6 19h14M6 24h9" stroke="#4d7cbc" stroke-width="2"/></svg>Articles</div>
      <div class="media-item"><div class="date">March 2018</div><div class="caption">Attendees listening to a speaker at the Common Table Dinner Dialogue event</div><div class="media-photo warm" role="img" aria-label="Photo of attendees at a dinner dialogue event"></div></div>
      <div class="media-item"><div class="date">April 2018</div><div class="caption">Students performing at the third annual Linden Park Arts Festival</div><div class="media-photo" role="img" aria-label="Photo of students performing at an arts festival"></div></div>
      <div class="load-more"><svg width="26" height="16" viewBox="0 0 26 16"><path d="M2 2l11 11L24 2" fill="none" stroke="#27374f" stroke-width="4"/></svg>Load More</div>
    </article>
    <article class="media-card">
      <div class="media-head"><svg width="32" height="26" viewBox="0 0 32 26"><rect x="1" y="1" width="30" height="24" rx="3" fill="none" stroke="#4d7cbc" stroke-width="2"/><path d="M13 8v10l8-5z" fill="#4d7cbc"/></svg>Videos</div>
      <div class="media-item"><div class="media-photo video" role="img" aria-label="Video still of a city street event"></div></div>
      <div class="media-item"><div class="media-photo video warm" role="img" aria-label="Video still of a group gathered outdoors"></div></div>
      <div class="load-more"><svg width="26" height="16" viewBox="0 0 26 16"><path d="M2 2l11 11L24 2" fill="none" stroke="#27374f" stroke-width="4"/></svg>Load More</div>
    </article>
    <article class="media-card">
      <div class="media-head"><svg width="30" height="30" viewBox="0 0 30 30"><circle cx="15" cy="13" r="4" fill="#4d7cbc"/><path d="M15 17v11" stroke="#4d7cbc" stroke-width="3"/><path d="M8 20a9 9 0 1 1 14 0M4 24a14 14 0 1 1 22 0" fill="none" stroke="#4d7cbc" stroke-width="2"/></svg>Podcasts</div>
      <div class="media-item"><div class="caption strong">Mara welcoming volunteers to the annual College orientation week service event</div><div class="media-photo" role="img" aria-label="Photo of a speaker welcoming volunteers"></div></div>
      <div class="media-item"><div class="caption strong">Mara introducing a dinner dialogue on the intersection of education and mental health</div><div class="media-photo warm" role="img" aria-label="Photo of a speaker at a dinner dialogue"></div></div>
      <div class="load-more"><svg width="26" height="16" viewBox="0 0 26 16"><path d="M2 2l11 11L24 2" fill="none" stroke="#27374f" stroke-width="4"/></svg>Load More</div>
    </article>
  </div>
</section>

<section class="contact">
  <h2 class="heading">CONTACT</h2>
  <div class="contact-text">
    <h3>Rates</h3>
    <p>Depending on the services requested, Mara offers an hourly rate, a package rate, or a retainer fee based on the scope and complexity of the project.</p>
    <h3>Book a complimentary consultation</h3>
    <p>Use the form below to tell Mara about your inquiry, and she will schedule a 30-minute meeting, phone call, or video chat to discuss your project outcomes.</p>
  </div>
  <div class="portrait" role="img" aria-label="Photo of Mara Ellison presenting at an event"></div>
</section>

<section class="message" role="img" aria-label="Blue-tinted photo behind the message form">
  <h2 class="section-title light">SEND A MESSAGE</h2>
  <div class="form-row">
    <div class="field">Your Name</div>
    <div class="field">Your Email</div>
    <div class="field">Your Subject</div>
  </div>
  <div class="field textarea">Message</div>
  <div class="send-btn">Send Message</div>
</section>

<footer class="site-footer">
  <div class="footer-brand"><span class="mark"></span><span class="name">VERDANT HARBOR ADVISORY</span></div>
  <nav class="footer-nav"><span>ABOUT</span><span>SERVICES &amp; TESTIMONIALS ▾</span><span>MEDIA &amp; IMPACT ▾</span><span>CONTACT</span></nav>
  <div class="bottom-bar">
    <span>COPYRIGHT © 2019 VERDANT HARBOR ADVISORY. ALL RIGHTS RESERVED.</span>
    <span class="social"><span></span><span></span><span></span></span>
  </div>
</footer>

</body>
</html>
```